Landing Page Design

We need a landing page template designed to support a clients Zintro Bidlink Campaigns. The client is called Merrow Plumbing and they install and repair hot water systems (only). They provide no other plumbing services.

We are really looking for a great looking landing page that is both engaging and functional.

Target Market(s)

Residential/Domestic market. Typically wives and partners who are typically home or run the household.

Industry/Entity Type

Plumbing

Number of Pages Required

1 page

Requirements
Must have
• Strong branding
Strong call to actions
Great and obvious looking buttons
Nice to have
• Smart use of colour
Should not have
• The design should not use old-style, serif fonts.

Do not include any plumbing images

```html
<!DOCTYPE html>
<html lang="en">
<head>
<meta charset="utf-8">
<title>Merrow Plumbing – Solar Hot Water Systems</title>
<link href="https://fonts.googleapis.com/css2?family=Arimo:wght@400;700&display=swap" rel="stylesheet">
<style>
  :root{
    --page:#f8f8f8;
    --header:#fdd062;
    --banner:#fbb829;
    --banner-light:#fcc445;
    --accent:#f04e23;
    --orange-top:#fba63a;
    --orange-bottom:#ef7f1e;
    --body:#f2f2f2;
    --title:#6b6b6b;
    --ink:#111;
    --footer:#717171;
    --field:#f2f2f2;
  }
  *{box-sizing:border-box;margin:0;padding:0}
  html,body{width:1079px;height:1200px;overflow:hidden;background:var(--page);font-family:Arimo,Arial,sans-serif;color:var(--ink)}
  .page{position:absolute;left:111px;top:0;width:854px;height:991px}
  .site-header{position:absolute;left:0;top:0;width:854px;height:171px;background:var(--header)}
  .brand{position:absolute;left:40px;top:70px;display:flex;align-items:center;gap:10px;color:var(--accent);font-size:34px;font-weight:700;letter-spacing:1px}
  .brand-dot{width:22px;height:22px;border-radius:50%;background:var(--accent)}
  .call{position:absolute;right:38px;top:56px;text-align:right;color:var(--accent)}
  .call-label{font-size:18px;display:flex;align-items:center;justify-content:flex-end;gap:4px;color:#f47a2a}
  .call-number{font-size:29px;margin-top:4px}
  .banner{position:absolute;left:0;top:171px;width:854px;height:151px;background:linear-gradient(90deg,var(--banner),var(--banner-light))}
  .lettering{position:absolute;left:64px;top:25px;width:462px;height:52px;border-radius:26px;background:rgba(255,255,255,.3)}
  .save{position:absolute;left:0;width:616px;top:92px;line-height:36px;text-align:center;color:#fff;font-size:32px}
  .perks{position:absolute;left:587px;top:9px;list-style:none;color:var(--accent);font-size:16px;line-height:26px}
  .content{position:absolute;left:0;top:322px;width:854px;height:648px;background:var(--body)}
  .title{position:absolute;left:40px;top:26px;font-size:32px;font-weight:400;color:var(--title);line-height:38px}
  .copy{position:absolute;left:40px;top:90px;width:245px;font-size:12.2px;line-height:21.6px}
  .copy p+p{margin-top:21.6px}
  .photo{position:absolute;left:301px;top:90px;width:243px;height:453px;background:linear-gradient(160deg,#e9e9e9 0%,#9c9c9c 45%,#5a5a5a 75%,#b58a78 100%)}
  .btn{position:absolute;display:flex;align-items:center;justify-content:center;gap:14px;height:44px;border-radius:4px;color:#fff;font-size:16px;letter-spacing:.5px;text-decoration:none;background:linear-gradient(var(--orange-top),var(--orange-bottom))}
  .btn-quote{left:40px;top:440px;width:239px}
  .btn-site{left:41px;top:499px;width:238px}
  .btn-rebates{left:41px;top:555px;width:503px}
  .enquiry{position:absolute;left:587px;top:30px;width:213px}
  .enquiry-intro{font-size:14.6px;line-height:16.3px;color:#111;white-space:nowrap;letter-spacing:.2px}
  .enquiry-intro em{font-style:normal;color:var(--accent)}
  .field label{display:block;font-size:10px;line-height:12px;position:absolute;left:0;white-space:nowrap}
  .field label span{color:var(--accent)}
  .field .input{position:absolute;left:0;width:213px;height:22px;border:1px solid #ccc;border-top:2px solid #9a9a9a;border-left:2px solid #b5b5b5;background:var(--field)}
  .btn-enquire{position:absolute;left:0;top:527px;width:213px;height:44px;border-radius:4px;background:linear-gradient(#f3f3f3,#d4d4d4);display:flex;align-items:center;justify-content:center;gap:14px;color:#f7941d;font-size:17px;letter-spacing:1px}
  .site-footer{position:absolute;left:0;top:970px;width:854px;height:21px;background:var(--footer);color:#fff;font-size:10px;letter-spacing:.4px;display:flex;align-items:center;justify-content:space-between;padding:0 8px}
  .site-footer nav a{color:#fff;margin-left:14px}
</style>
</head>
<body>
<div class="page">
  <header class="site-header">
    <div class="brand"><span class="brand-dot"></span>MERROW</div>
    <div class="call">
      <div class="call-label">
        <svg width="18" height="18" viewBox="0 0 18 18"><path d="M3 15c5-3 9-7 12-12l2 2c-3 5-7 9-12 12z" fill="var(--accent)"/></svg>
        Call NOW on
      </div>
      <div class="call-number">9000 4127</div>
    </div>
  </header>

  <section class="banner">
    <div class="lettering" role="img" aria-label="Hand lettered slogan: Hot water now!"></div>
    <div class="save">SAVE $$$</div>
    <ul class="perks">
      <li>Sydney 24 Hours 7 Days</li>
      <li>On Time</li>
      <li>Professional Technicians</li>
      <li>We Advise on Rebates</li>
      <li>Authorised Corvel Dealer</li>
    </ul>
  </section>

  <main class="content">
    <h1 class="title">Solar Hot Water Systems</h1>
    <div class="copy">
      <p>Engage our routine office cleaning for at least 6 months and receive a FREE Carpet and Window clean! No strings attached, no contracts.</p>
      <p>To take advantage of this great offer call us on 1300 00 41 27 or complete and submit the form on this page.</p>
      <p>At Harlow Services we provide all your property service needs - painlessly. We understand that cleaning and other property services should be background activities. A set and forget proposition.</p>
    </div>
    <div class="photo" role="img" aria-label="Photo of a woman enjoying a hot shower"></div>

    <a class="btn btn-quote" href="#">
      <svg width="24" height="28" viewBox="0 0 24 28"><path d="M2 1h14l6 6v20H2z" fill="none" stroke="#fff" stroke-width="2"/><path d="M7 20l4-6 4 6" fill="none" stroke="#fff" stroke-width="1.5"/></svg>
      Book a FREE Quote
    </a>
    <a class="btn btn-site" href="#">
      <svg width="26" height="26" viewBox="0 0 26 26" fill="none" stroke="#fff" stroke-width="1.5"><circle cx="13" cy="13" r="11"/><ellipse cx="13" cy="13" rx="5" ry="11"/><path d="M2 13h22M4 7h18M4 19h18"/></svg>
      Visit Our Web Site
    </a>
    <a class="btn btn-rebates" href="#">Click here for information on Rebates</a>

    <form class="enquiry">
      <p class="enquiry-intro">Take advantage of this great<br>offer. Contact Us <em>NOW</em> on<br><em>9000 4127</em> or register<br>your interest below</p>
      <div class="field"><label style="top:89px">Your First Name: <span>*</span></label><div class="input" style="top:107px"></div></div>
      <div class="field"><label style="top:143px">Your Surname: <span>*</span></label><div class="input" style="top:160px"></div></div>
      <div class="field"><label style="top:203px">Your Suburb: <span>*</span></label><div class="input" style="top:221px"></div></div>
      <div class="field"><label style="top:258px">Best Contact Number: <span>*</span></label><div class="input" style="top:276px"></div></div>
      <div class="field"><label style="top:313px">Your Email Address: <span>*</span></label><div class="input" style="top:330px"></div></div>
      <div class="field"><label style="top:366px">Enquiry / Comments: <span>*</span></label><div class="input" style="top:383px;height:113px"></div></div>
      <div class="btn-enquire">
        <svg width="32" height="20" viewBox="0 0 32 20" fill="none" stroke="#777" stroke-width="1.6"><path d="M2 6h6l4-4h6v4h12v4H18v8H10l-8-2z"/></svg>
        ENQUIRE NOW
      </div>
    </form>
  </main>

  <footer class="site-footer">
    <span>MERROW PLUMBING | HOT WATER SOLUTIONS</span>
    <nav><a href="#">INFORMATION ON REBATES</a><a href="#">BOOK A FREE QUOTE</a><a href="#">VISIT OUR WEB SITE NOW</a></nav>
  </footer>
</div>
</body>
</html>
```